Home Health Care Agency Needs a Website (Seeking a PSD)

We need a user friendly website for a Home Health Care Agency. Our service is for the elderly and disabled. Frequently the busy professional middle-aged married daughter will use the website to arrange in-home care for an aging parent. Therefore, our website is primarily geared towards middle-aged women. In-home care is typically 24 hours a day so, a feeling of trustworthiness and security should be effectively conveyed. (Seeking a PSD- however, if you also offer coding, please let us know the cost.)

Target Market(s)

Frequently the busy professional middle-aged married daughter (possibly out of state) will use the website to arrange in-home care for an aging parent.

Industry/Entity Type

Security

Requirements
Must have
• Website must be clean, uncluttered and professional. The following menu pages are requested: Home, About Us, Services, Resources, FAQ, Employment & Contact.
Should not have
• Must not be too whimsical.

```html
<!DOCTYPE html>
<html lang="en">
<head>
<meta charset="utf-8">
<title>Harbor Home Health</title>
<link href="https://fonts.googleapis.com/css2?family=Roboto:wght@300;400;500;700&display=swap" rel="stylesheet">
<style>
:root{
  --blue:#4ac5ee;
  --ink:#555a5e;
  --ink-soft:#7a7f83;
  --heading:#5b6066;
  --panel:#f6f6f6;
  --line:#e2e2e2;
  --footer:#6e6f72;
  --footer-text:#d6d7d9;
  --black:#111;
  --white:#fff;
}
*{margin:0;padding:0;box-sizing:border-box}
html,body{width:894px;height:1200px;overflow:hidden}
body{font-family:"Roboto",Arial,sans-serif;color:var(--ink);background:var(--white);position:relative}
.abs{position:absolute}
a{color:inherit;text-decoration:none}

/* header */
.site-header{left:0;top:0;width:894px;height:91px;background:var(--white)}
.brand{left:120px;top:28px;display:flex;align-items:center;gap:8px}
.brand-mark{width:22px;height:22px;border-radius:50%;background:var(--blue)}
.brand-name{font-size:19px;font-weight:500;color:var(--blue);letter-spacing:-.2px}
.main-nav{left:354px;top:0;height:91px;display:flex}
.main-nav a{font-size:11px;color:var(--ink);height:91px;line-height:91px;padding:0 11px}
.main-nav a.active{background:#f3f3f3;position:relative;padding:0 13px}
.main-nav a.active::after{content:"";position:absolute;left:0;right:0;bottom:0;height:4px;background:var(--blue)}
.main-nav a.active::before{content:"";position:absolute;left:50%;bottom:4px;margin-left:-4px;border:4px solid transparent;border-bottom-color:var(--blue);border-top:0}

/* hero */
.hero{left:0;top:91px;width:894px;height:363px;background:linear-gradient(100deg,#3a3a3a 0%,#8d8d8d 25%,#bdbdbd 45%,#9a9a9a 65%,#d8d8d8 100%)}
.hero-caption{left:120px;top:249px;height:46px;display:flex}
.hero-caption .title{width:370px;background:var(--blue);color:var(--white);font-size:20px;font-weight:500;line-height:46px;padding-left:19px}
.hero-caption .badge{width:59px;background:var(--black);color:var(--white);font-size:19px;font-weight:300;line-height:46px;text-align:center}
.hero-caption .badge small{font-size:10px}
.slider-dots{left:421px;top:415px;display:flex;gap:6px}
.slider-dots span{width:12px;height:12px;border-radius:50%;background:var(--white)}
.slider-dots span.on{background:var(--blue)}

/* section headings */
.section-title{font-size:19px;font-weight:400;color:var(--heading);letter-spacing:.2px}
.section-title b{font-weight:700}

/* services */
.services-title{left:120px;top:479px}
.services-arrows{left:754px;top:481px}
.service{top:524px;width:220px}
.service .icon{position:absolute;left:0;top:0;width:72px;height:72px;border-radius:50%;background:var(--blue)}
.service .icon svg{position:absolute;left:20px;top:20px}
.service .body{position:absolute;left:86px;top:6px;width:136px}
.service h3{font-size:13px;font-weight:400;color:var(--heading);margin-bottom:6px}
.service p{font-size:8.5px;line-height:12px;color:var(--ink-soft)}
.service .more{display:block;font-size:8.5px;color:var(--blue);margin-top:7px}

/* about + faq band */
.band{left:0;top:646px;width:894px;height:359px;background:var(--panel)}
.about-title{left:120px;top:684px}
.about-photo{left:120px;top:718px;width:420px;height:123px;background:var(--white);border:1px solid var(--line);padding:4px}
.about-photo div{width:100%;height:100%;background:linear-gradient(90deg,#3b3a44 0%,#a37560 35%,#d2a287 60%,#e9e1d6 100%)}
.about-text{left:120px;top:853px;width:420px;font-size:8.8px;line-height:13.4px;color:var(--ink-soft)}
.about-more{left:120px;top:942px;font-size:8.8px;color:var(--blue);text-decoration:underline}
.faq-title{left:573px;top:684px}
.faq-box{left:570px;top:718px;width:204px;height:240px;background:var(--white);border:1px solid var(--line)}
.faq-item{position:absolute;left:14px;width:176px}
.faq-item .num{position:absolute;left:0;top:2px;width:19px;height:19px;background:var(--blue);color:var(--white);font-family:Georgia,serif;font-size:10px;text-align:center;line-height:19px}
.faq-item h4{margin-left:29px;font-size:8.8px;font-weight:400;color:var(--ink);margin-bottom:4px}
.faq-item p{margin-left:29px;font-size:8.4px;line-height:13.4px;color:var(--ink-soft)}
.faq-rule{position:absolute;left:14px;top:114px;width:178px;height:1px;background:var(--line)}
.faq-more{position:absolute;right:18px;top:210px;font-size:8.8px;color:var(--blue);text-decoration:underline}

/* footer */
.site-footer{left:0;top:1005px;width:894px;height:165px;background:var(--footer)}
.footer-title{font-size:13px;font-weight:400;color:#f2f2f2;top:1045px}
.footer-list{list-style:none;top:1071px}
.footer-list li{font-size:8.8px;color:var(--footer-text);height:19px;display:flex;align-items:center;gap:6px}
.footer-list .caret{width:0;height:0;border:3px solid transparent;border-left:3px solid var(--footer-text);border-right:0}
.footer-list li.current{color:var(--blue)}
.footer-list li.current .caret{border-left-color:var(--blue)}
.footer-list .ico{width:10px;display:inline-flex;justify-content:center}
.social li{justify-content:space-between;width:64px}
.social .dot{width:6px;height:6px;border-radius:50%;background:var(--footer-text)}
.copyright{left:0;top:1170px;width:894px;height:30px;background:var(--blue);color:var(--white);font-size:8.8px;line-height:30px;padding-left:120px}
</style>
</head>
<body>

<header class="site-header abs">
  <div class="brand abs"><span class="brand-mark"></span><span class="brand-name">Harbor Home Health</span></div>
  <nav class="main-nav abs">
    <a class="active" href="#">Home</a>
    <a href="#">About Us</a>
    <a href="#">Services</a>
    <a href="#">Resources</a>
    <a href="#">FAQ</a>
    <a href="#">Employment &amp; Contact</a>
  </nav>
</header>

<section class="hero abs" role="img" aria-label="Black and white photo of a younger hand holding an elderly person's hand"></section>
<div class="hero-caption abs">
  <div class="title">We are careing old-aged People</div>
  <div class="badge">24<small>Hr</small></div>
</div>
<div class="slider-dots abs"><span class="on"></span><span></span><span></span></div>

<h2 class="section-title services-title abs"><b>OUR</b> SERVICES</h2>
<svg class="services-arrows abs" width="18" height="12" viewBox="0 0 18 12">
  <path d="M6 1 1 6l5 5" fill="none" stroke="var(--blue)" stroke-width="1.6"/>
  <path d="M12 1l5 5-5 5" fill="none" stroke="var(--heading)" stroke-width="1.6"/>
</svg>

<div class="service abs" style="left:120px">
  <div class="icon"><svg width="32" height="32" viewBox="0 0 32 32"><circle cx="16" cy="16" r="13" fill="none" stroke="#fff" stroke-width="3"/><path d="M16 8v9h-5" fill="none" stroke="#fff" stroke-width="3"/></svg></div>
  <div class="body">
    <h3>24hr Nursing care</h3>
    <p>Lorem Ipsum is simply dummy text of the printing and typesetting industry.</p>
    <a class="more" href="#">Read More</a>
  </div>
</div>
<div class="service abs" style="left:345px">
  <div class="icon"><svg width="32" height="32" viewBox="0 0 32 32"><path d="M2 16 16 4l14 12" fill="none" stroke="#fff" stroke-width="3.5"/><path d="M7 15v13h7v-8h4v8h7V15L16 7z" fill="#fff"/></svg></div>
  <div class="body">
    <h3>Home care Service</h3>
    <p>Ipsum has been the industry's standard dummy text ever since the 1500s, when an</p>
    <a class="more" href="#">Read More</a>
  </div>
</div>
<div class="service abs" style="left:569px">
  <div class="icon"><svg width="32" height="32" viewBox="0 0 32 32"><path d="M16 5c-4 6-8 11-8 15a8 8 0 0 0 16 0c0-4-4-9-8-15z" fill="#fff"/></svg></div>
  <div class="body">
    <h3>Retirement Homes</h3>
    <p>Simply dummy text of the printing and typesetting industry. Lorem Ipsum has been the</p>
    <a class="more" href="#">Read More</a>
  </div>
</div>

<section class="band abs"></section>
<h2 class="section-title about-title abs"><b>ABOUT</b> US</h2>
<div class="about-photo abs"><div role="img" aria-label="Close-up photo of an elderly hand clasped by a caregiver's hand"></div></div>
<p class="about-text abs">There are many variations of passages of Lorem Ipsum available, but the majority have suffered alteration in some form, by injected humour, or randomised words which don't look even slightly believable. If you are going to use a passage of Lorem Ipsum, you need to be sure there isn't anything embarrassing hidden in the middle of text. All the Lorem Ipsum generators on the Internet tend to repeat predefined chunks as necessary, making this the first true generator on the Internet. It uses a dictionary of over 200 Latin words, combined with a handful of model sentence structures</p>
<a class="about-more abs" href="#">Read More</a>

<h2 class="section-title faq-title abs"><b>FAQ</b>S</h2>
<div class="faq-box abs">
  <div class="faq-item" style="top:18px">
    <span class="num">1</span>
    <h4>There are many variations of pass ?</h4>
    <p>be sure there isn't anything embarrassing hidden in the middle of text. All the Lorem Ipsum generators on the Internet tend to repeat predefined chunks as necessary,</p>
  </div>
  <div class="faq-rule"></div>
  <div class="faq-item" style="top:131px">
    <span class="num">2</span>
    <h4>Dictionary of over 200 Latin words ?</h4>
    <p>be sure there isn't anything embarrassing hidden in the middle of text. All the Lorem Ipsum generators on</p>
  </div>
  <a class="faq-more" href="#">View More</a>
</div>

<footer class="site-footer abs"></footer>
<h3 class="footer-title abs" style="left:119px">Navigation</h3>
<ul class="footer-list abs" style="left:119px">
  <li class="current"><span class="caret"></span>Home</li>
  <li><span class="caret"></span>About Us</li>
  <li><span class="caret"></span>Services</li>
</ul>
<ul class="footer-list abs" style="left:254px">
  <li><span class="caret"></span>Resources</li>
  <li><span class="caret"></span>FAQ</li>
  <li><span class="caret"></span>Employment &amp; Contact</li>
</ul>
<h3 class="footer-title abs" style="left:462px">Contact Details</h3>
<ul class="footer-list abs" style="left:464px">
  <li><span class="ico"><svg width="7" height="9" viewBox="0 0 7 9"><path d="M3.5 0A3.5 3.5 0 0 0 0 3.5C0 6 3.5 9 3.5 9S7 6 7 3.5A3.5 3.5 0 0 0 3.5 0zm0 5a1.5 1.5 0 1 1 0-3 1.5 1.5 0 0 1 0 3z" fill="#d6d7d9"/></svg></span>Address</li>
  <li><span class="ico"><svg width="9" height="9" viewBox="0 0 9 9"><path d="M2 0 0 1.5C.5 5 4 8.5 7.5 9L9 7 7 5.5 5.8 6.6C4.5 6 3 4.5 2.4 3.2L3.5 2z" fill="#d6d7d9"/></svg></span>+1 555-0142-300</li>
  <li><span class="ico"><svg width="9" height="7" viewBox="0 0 9 7"><rect width="9" height="7" fill="#d6d7d9"/><path d="M0 0l4.5 4L9 0" fill="none" stroke="#6e6f72"/></svg></span>help@harborcare.com</li>
</ul>
<h3 class="footer-title abs" style="left:689px">Follow us on</h3>
<ul class="footer-list social abs" style="left:689px">
  <li>Blog<span class="dot"></span></li>
  <li>News<span class="dot"></span></li>
  <li>Community<span class="dot"></span></li>
</ul>
<div class="copyright abs">Copyright © 2013 home helath Allright Reserved</div>

</body>
</html>
```